Clean business card with logo provided

I want a card that will stand out among the masses. I need the color and image to show professionalism and yet have a family appeal showing that I only deal with win/win scenarios. The back of the card will be used to take notes about the individual so I can use that in my database entry. I like modern design but need professionalism in it also. It needs to fit my "clean, safe, and affordable housing" motto. I need to be able to write on the file and update the card details for my employees.

Target Market(s)

Investors looking to make investment income through real estate

Industry/Entity Type

Real Estate

Contact Information for Business Card

Mark Dunthorpe
blank address, city, st, zip code
480-555-3174
markdunthorpe@brivoholdings.example
www.brivoholdings.example

Font styles to use
Sans Serif

Requirements
Must have
• I would like the back of the card to have lines for info. example
• Met/Visited: Date:
• Interets:
Nice to have
• I want the cards color to match the logo background color. Font with details to be san serif and black. I want the card rectangular with square corners. Standard business card size. I would like to see cards designed with both images to see which i prefer more.

```html
<!DOCTYPE html>
<html lang="en">
<head>
<meta charset="utf-8">
<title>Brivo Holdings LLC – Business Card</title>
<link href="https://fonts.googleapis.com/css2?family=Fira+Sans:wght@400;500;700&display=swap" rel="stylesheet">
<style>
  :root {
    --teal: #0fb3cb;
    --ink: #161616;
    --white: #ffffff;
    --paper: #e9e9e7;
    --rule: #0fb3cb;
  }
  * { box-sizing: border-box; margin: 0; padding: 0; }
  html, body {
    width: 1200px; height: 873px; overflow: hidden;
    background: var(--paper);
    font-family: "Fira Sans", Arial, sans-serif;
  }
  .sheet {
    position: relative; width: 1200px; height: 873px;
    display: flex; align-items: center; justify-content: center; gap: 60px;
  }
  .card {
    position: relative; width: 520px; height: 297px;
    box-shadow: 0 6px 18px rgba(0,0,0,.12);
    overflow: hidden;
  }

  /* Front */
  .card--front { background: var(--teal); }
  .brand { position: absolute; display: flex; align-items: center; gap: 10px; }
  .brand__dot { width: 14px; height: 14px; border-radius: 50%; background: var(--ink); flex: none; }
  .brand__name {
    font-weight: 500; color: var(--ink); letter-spacing: .12em;
    text-transform: uppercase; white-space: nowrap;
  }
  .tagline { position: absolute; color: var(--white); font-size: 11px; letter-spacing: .02em; }
  .card--front .brand { left: 40px; top: 52px; }
  .card--front .brand__name { font-size: 27px; }
  .card--front .tagline { left: 64px; top: 92px; }

  .divider { position: absolute; left: 250px; top: 150px; width: 1.5px; height: 110px; background: var(--ink); }
  .contact { position: absolute; left: 272px; top: 166px; }
  .contact__name { font-size: 20px; color: var(--ink); margin-bottom: 10px; }
  .contact__name b { font-weight: 700; }
  .contact__list { list-style: none; }
  .contact__item {
    display: flex; align-items: center; gap: 7px;
    font-size: 11px; color: var(--white); line-height: 18px; white-space: nowrap;
  }
  .contact__icon { width: 10px; height: 10px; flex: none; }

  /* Back */
  .card--back { background: var(--white); }
  .band { position: absolute; left: 0; top: 0; width: 168px; height: 100%; background: var(--teal); }
  .card--back .brand { left: 14px; top: 120px; gap: 6px; }
  .card--back .brand__dot { width: 8px; height: 8px; }
  .card--back .brand__name { font-size: 12.5px; letter-spacing: .08em; }
  .card--back .tagline { left: 14px; top: 142px; font-size: 6.5px; width: 150px; }

  .notes { position: absolute; left: 196px; top: 0; width: 300px; height: 100%; }
  .field { position: absolute; left: 0; width: 100%; display: flex; align-items: flex-end; gap: 8px; }
  .field__label { font-size: 14px; font-weight: 500; color: var(--teal); white-space: nowrap; }
  .field__line { flex: 1; height: 10px; }
  .field--met { top: 48px; }
  .field--date { top: 96px; }
  .field--interests { top: 144px; }
  .field--blank-1 { top: 192px; }
  .field--blank-2 { top: 240px; }
</style>
</head>
<body>
<main class="sheet">

  <section class="card card--front" aria-label="Card front">
    <div class="brand">
      <span class="brand__dot"></span>
      <span class="brand__name">Brivo Holdings LLC</span>
    </div>
    <p class="tagline">Providing clean, safe, and affordable housing</p>

    <div class="divider"></div>

    <div class="contact">
      <p class="contact__name"><b>Mark</b> Dunthorpe</p>
      <ul class="contact__list">
        <li class="contact__item">
          <svg class="contact__icon" viewBox="0 0 10 10"><path d="M5 0.5a3.2 3.2 0 0 1 3.2 3.2C8.2 6.2 5 9.5 5 9.5S1.8 6.2 1.8 3.7A3.2 3.2 0 0 1 5 0.5z" fill="#fff"/><circle cx="5" cy="3.7" r="1.2" fill="#0fb3cb"/></svg>
          blank address, city, st, zip code
        </li>
        <li class="contact__item">
          <svg class="contact__icon" viewBox="0 0 10 10"><path d="M2 0.8l1.8 0.2.6 2.2-1.1.8a6 6 0 0 0 2.7 2.7l.8-1.1 2.2.6.2 1.8c0 .6-.5 1-1 1A8.2 8.2 0 0 1 1 1.8c0-.5.4-1 1-1z" fill="#fff"/></svg>
          480-555-3174
        </li>
        <li class="contact__item">
          <svg class="contact__icon" viewBox="0 0 10 10"><rect x="0.5" y="2" width="9" height="6.4" fill="#fff"/><path d="M0.8 2.3L5 5.6l4.2-3.3" stroke="#0fb3cb" stroke-width="0.9" fill="none"/></svg>
          markdunthorpe@brivoholdings.example
        </li>
      </ul>
    </div>
  </section>

  <section class="card card--back" aria-label="Card back">
    <div class="band"></div>
    <div class="brand">
      <span class="brand__dot"></span>
      <span class="brand__name">Brivo Holdings LLC</span>
    </div>
    <p class="tagline">Providing clean, safe, and affordable housing</p>

    <div class="notes">
      <div class="field field--met">
        <span class="field__label">Met/Visited:</span>
        <svg class="field__line" viewBox="0 0 200 10" preserveAspectRatio="none"><line x1="0" y1="9" x2="194" y2="9" stroke="#0fb3cb" stroke-width="1"/><path d="M192 5l8 4-8 4z" fill="#0fb3cb"/></svg>
      </div>
      <div class="field field--date">
        <span class="field__label">Date:</span>
        <svg class="field__line" viewBox="0 0 200 10" preserveAspectRatio="none"><line x1="0" y1="9" x2="194" y2="9" stroke="#0fb3cb" stroke-width="1"/><path d="M192 5l8 4-8 4z" fill="#0fb3cb"/></svg>
      </div>
      <div class="field field--interests">
        <span class="field__label">Interests:</span>
        <svg class="field__line" viewBox="0 0 200 10" preserveAspectRatio="none"><line x1="0" y1="9" x2="194" y2="9" stroke="#0fb3cb" stroke-width="1"/><path d="M192 5l8 4-8 4z" fill="#0fb3cb"/></svg>
      </div>
      <div class="field field--blank-1">
        <svg class="field__line" viewBox="0 0 300 10" preserveAspectRatio="none"><line x1="0" y1="9" x2="294" y2="9" stroke="#0fb3cb" stroke-width="1"/><path d="M292 5l8 4-8 4z" fill="#0fb3cb"/></svg>
      </div>
      <div class="field field--blank-2">
        <svg class="field__line" viewBox="0 0 300 10" preserveAspectRatio="none"><line x1="0" y1="9" x2="294" y2="9" stroke="#0fb3cb" stroke-width="1"/><path d="M292 5l8 4-8 4z" fill="#0fb3cb"/></svg>
      </div>
    </div>
  </section>

</main>
</body>
</html>
```